ecommerce news podcast artwork

Podcast cover art for a podcast featuring daily news and events around ecommerce product businesses.

text to be: VORLA BEAT
optional third line of text with smaller font: Podcast

looking for something that pops with a medium to light blue background. text can be in white/red/orange colors. prefer solid colors for text, but background can vary.
I'm really open to other ideas too, sometimes you don't know what you want until you see it.

Target Market(s)

ecommerce business owners, managers

Industry/Entity Type

news, business, ecommerce

Font styles to use
Sans Serif

Colors
0054AA
0677BA
7BADD7
CADEEF
E8F1F8
0094D4
00A9DD
6FCCEA
C7EBF8
E9F6FB
F0912C
F2A743
F7CA91
FBE8D2
FDF5EE
EB3D1F
EC4F4E
F09395
F8D3D4
FCEDEE

Requirements
Must have
• text: VORLA BEAT
Should not have
• no microphones, headsets/headphones, speakers, or other props like that.

```html
<!DOCTYPE html>
<html lang="en">
<head>
<meta charset="utf-8">
<title>Vorla Beat Podcast Cover</title>
<link rel="stylesheet" href="https://fonts.googleapis.com/css2?family=Titan+One&family=Josefin+Sans:wght@600&display=swap">
<style>
  :root {
    --mat-navy: #303657;
    --sky-edge: #8fdef6;
    --sky-mid: #c7ebf8;
    --sky-glow: #f4fcff;
    --title-black: #050505;
    --title-orange: #ff6a05;
    --label-black: #111111;
  }
  html, body {
    margin: 0;
    padding: 0;
    width: 1200px;
    height: 1200px;
    overflow: hidden;
    background: var(--mat-navy);
  }
  .cover {
    position: absolute;
    left: 143px;
    top: 143px;
    width: 914px;
    height: 914px;
    background: radial-gradient(circle at 50% 55%, var(--sky-glow) 0%, var(--sky-mid) 38%, var(--sky-edge) 100%);
    overflow: hidden;
  }
  .cover-title {
    position: absolute;
    inset: 0;
    width: 914px;
    height: 914px;
  }
  .title-line {
    font-family: "Titan One", sans-serif;
  }
  .title-line--top { fill: var(--title-black); }
  .title-line--bottom { fill: var(--title-orange); }
  .show-label {
    font-family: "Josefin Sans", sans-serif;
    font-weight: 600;
    fill: var(--label-black);
    letter-spacing: 20px;
  }
</style>
</head>
<body>
  <main class="cover" role="img" aria-label="Light blue sunburst background with the Vorla Beat podcast title">
    <svg class="cover-title" viewBox="0 0 914 914" xmlns="http://www.w3.org/2000/svg">
      <text class="title-line title-line--top" x="75" y="373" font-size="215" textLength="765" lengthAdjust="spacingAndGlyphs">VORLA</text>
      <text class="title-line title-line--bottom" x="68" y="640" font-size="290" textLength="780" lengthAdjust="spacingAndGlyphs">BEAT</text>
      <text class="show-label" x="468" y="739" font-size="46" text-anchor="middle">PODCAST</text>
    </svg>
  </main>
</body>
</html>
```